Simple AD for Digital Publication

Total Size 5" x 5", may include boarder or not
Image Provided; crop or use as background
Incorporate Logo and text as provided

Target Market(s)

Sound Contractors / Integrators

Industry/Entity Type

Audio Video Lighting

Requirements
Must have
• Bold Look that reflects our brand. see website: tovermundic.com - cohesive text and style

```html
<!DOCTYPE html>
<html lang="en">
<head>
<meta charset="utf-8">
<title>Tovermundic Co – Become a Dealer</title>
<link rel="stylesheet" href="https://fonts.googleapis.com/css2?family=Montserrat:wght@500;700;800&display=swap">
<style>
  :root {
    --page-bg: #a3a3aa;
    --ad-black: #050505;
    --brand-red: #b01c22;
    --brand-red-light: #d8474c;
    --accent-yellow: #f5c400;
    --text-white: #ffffff;
    --text-dark: #1e1e22;
    --header-white: #f7f7fa;
  }
  html, body {
    margin: 0;
    padding: 0;
    width: 1200px;
    height: 1117px;
    overflow: hidden;
    background: var(--page-bg);
    font-family: "Montserrat", sans-serif;
  }
  .ad {
    position: absolute;
    left: 41px;
    top: 0;
    width: 1117px;
    height: 1117px;
    background: var(--ad-black);
    overflow: hidden;
  }
  .ad-art {
    position: absolute;
    inset: 0;
    width: 1117px;
    height: 1117px;
  }
  .brand-header {
    position: absolute;
    left: 176px;
    top: 0;
    width: 769px;
    height: 151px;
    background: var(--header-white);
    clip-path: polygon(0 0, 100% 0, 91.7% 100%, 8.8% 100%);
    display: flex;
    align-items: center;
    justify-content: center;
    gap: 18px;
  }
  .brand-square {
    width: 52px;
    height: 52px;
    background: var(--brand-red);
  }
  .brand-text { display: flex; flex-direction: column; line-height: 1; }
  .brand-name {
    font-weight: 800;
    font-size: 50px;
    color: var(--text-dark);
    letter-spacing: -1px;
  }
  .brand-tagline {
    margin-top: 6px;
    font-weight: 700;
    font-size: 23px;
    color: var(--text-dark);
  }
  .headline {
    position: absolute;
    left: 0;
    width: 100%;
    text-align: center;
    top: 752px;
    line-height: 1;
  }
  .headline-kicker {
    font-weight: 800;
    font-size: 46px;
    color: var(--accent-yellow);
  }
  .headline-main {
    margin-top: 8px;
    font-weight: 800;
    font-size: 64px;
    line-height: 62px;
    color: var(--text-white);
  }
  .dealer-line {
    position: absolute;
    top: 960px;
    left: 0;
    width: 100%;
    margin: 0;
    text-align: center;
    font-size: 29px;
    font-weight: 500;
    color: var(--text-white);
  }
  .dealer-line strong { font-weight: 800; }
  .cta-button {
    position: absolute;
    left: 369px;
    top: 1000px;
    width: 382px;
    height: 78px;
    border-radius: 39px;
    background: var(--brand-red);
    box-shadow: inset 0 0 0 4px var(--brand-red-light);
    color: var(--text-white);
    font-weight: 800;
    font-size: 52px;
    display: flex;
    align-items: center;
    justify-content: center;
  }
</style>
</head>
<body>
  <main class="ad">
    <svg class="ad-art" viewBox="0 0 963 962" preserveAspectRatio="none">
      <defs>
        <linearGradient id="photoTone" x1="0" y1="0" x2="0.6" y2="1">
          <stop offset="0" stop-color="#12203f"/>
          <stop offset="0.3" stop-color="#2f4a26"/>
          <stop offset="0.6" stop-color="#6b5a3a"/>
          <stop offset="1" stop-color="#b89a86"/>
        </linearGradient>
        <linearGradient id="sideShade" x1="0" y1="0" x2="1" y2="1">
          <stop offset="0" stop-color="#3a3a3c"/>
          <stop offset="1" stop-color="#050505"/>
        </linearGradient>
      </defs>
      <polygon class="side-shade" points="0,360 300,620 0,760" fill="url(#sideShade)"/>
      <polygon class="stage-photo" role="img" aria-label="Photo of a stage floor pocket with cables, beside a garland with warm string lights"
        points="0,0 963,0 963,500 660,555 635,528 325,610 0,345" fill="url(#photoTone)"/>
      <polyline class="red-band" points="0,345 325,610 635,528 660,555 963,500"
        fill="none" stroke="#b01c22" stroke-width="18" stroke-linejoin="miter"/>
      <polygon class="corner-accent" points="670,962 963,897 963,962" fill="#b01c22"/>
    </svg>

    <header class="brand-header">
      <span class="brand-square"></span>
      <div class="brand-text">
        <span class="brand-name">TOVERMUNDIC CO</span>
        <span class="brand-tagline">Stage Pocket Systems Connectivity</span>
      </div>
    </header>

    <section class="headline">
      <div class="headline-kicker">PROTECT AND CONCEAL</div>
      <div class="headline-main">HIGH AND LOW VOLTAGE<br>CONNECTIVITY</div>
    </section>

    <p class="dealer-line">Become a <strong>Dealer</strong></p>
    <div class="cta-button">CLICK HERE</div>
  </main>
</body>
</html>
```